Verpackungen für Parfum-Proben
Besten Dank! Das Team ist begeistert - also bin ich es auch und wir freuen uns schon, unsere Parfum Proben in Zukunft in diesem tollen Design weitergeben zu können! Danke!
Zielgruppe
Hallo allerseits! Wir sind im Direktvertrieb in den Bereichen Parfum & Kosmetik tätig.
Aufgabenstellung
Für unsere Parfum-Proben benötige ich ein ansprechendes, modernes Design.
Das Design muss relativ neutral gehalten werden, da die Blister sowohl für Herren- als auch Damenproben verwendet werden.
Auf Vorder- und Rückseite soll unser Team-Logo (RuchKontor®) sichtbar sein (Vorderseite größer, Rückseite kleiner).
Auf der linken Innenseite sollte Plätz für einen netten Spruch (den ich mir noch überlege) sein.
Auf der Rückseite muss Platz (weißes / helles Feld) für einen Stempel und/oder Aufkleber (Kontaktdaten des Distributors) sein.
Unser Logo ist Lila - Das farbliche Design sollte dazu passen.
Bei Fragen, einfach Nachricht :)
Daten:
Endformat: 133 x 74 mm
Datenformat: 139 x 80 mm
1-teilig, gestanzt, genutet, einseitig geklebt geliefert
Bitte verwenden Sie für positive Schriftstärken mindestens 9pt (ca. 3,17mm) und bei negativen Schriftstärken mindestens 13pt (ca. 4,59mm).
Abmessungen / Druck- / Designvorlage, Logo, etc.: https://dateiwolke.example/ordner/X7KPtrWQ#m4vbeLhNcyrGzzt9_k2w8p

```html
<!DOCTYPE html>
<html lang="de">
<head>
<meta charset="utf-8">
<title>RuchKontor – Probenverpackung</title>
<link href="https://fonts.googleapis.com/css2?family=Open+Sans:wght@400;600&display=swap" rel="stylesheet">
<style>
  :root {
    --brand-purple: #6b56a3;
    --brand-purple-mid: #8c7cc0;
    --brand-lavender: #cdc4e6;
    --brand-mist: #ebe6f5;
    --paper: #ffffff;
    --stage: #ffffff;
    --fold-line: #555555;
  }
  * { box-sizing: border-box; margin: 0; padding: 0; }
  html, body {
    width: 1200px;
    height: 818px;
    overflow: hidden;
    background: var(--stage);
    font-family: "Open Sans", sans-serif;
  }
  .dieline {
    position: absolute;
    left: 232px;
    top: 207px;
    width: 735px;
    height: 404px;
    display: flex;
    border: 1px solid var(--fold-line);
  }
  .panel {
    position: relative;
    width: 50%;
    height: 100%;
    background: var(--paper);
    overflow: hidden;
  }
  .panel--front { border-left: 1px solid var(--fold-line); }
  .panel__art {
    position: absolute;
    inset: 0;
    width: 100%;
    height: 100%;
  }
  .wordmark {
    position: absolute;
    left: 0;
    right: 0;
    text-align: center;
    color: var(--brand-purple);
    font-weight: 400;
    letter-spacing: 0.01em;
    white-space: nowrap;
  }
  .wordmark--small { top: 108px; font-size: 24px; }
  .wordmark--large { top: 90px; font-size: 44px; }
  .sample-note {
    position: absolute;
    left: 250px;
    top: 342px;
    color: var(--paper);
    font-size: 19px;
    line-height: 24px;
    font-weight: 400;
    text-transform: uppercase;
  }
</style>
</head>
<body>
  <main class="dieline">
    <section class="panel panel--back" aria-label="Rückseite">
      <svg class="panel__art" viewBox="0 0 397 438" preserveAspectRatio="none" aria-hidden="true">
        <defs>
          <linearGradient id="back-swoosh" x1="0" y1="0" x2="1" y2="0">
            <stop offset="0" stop-color="#9283c3"/>
            <stop offset="1" stop-color="#e4dff2"/>
          </linearGradient>
          <linearGradient id="back-fade" x1="0" y1="0" x2="0" y2="1">
            <stop offset="0" stop-color="#ffffff"/>
            <stop offset="1" stop-color="#d5cce9"/>
          </linearGradient>
          <linearGradient id="back-base" x1="0" y1="0" x2="1" y2="0">
            <stop offset="0" stop-color="#8372b8"/>
            <stop offset="1" stop-color="#ece8f6"/>
          </linearGradient>
        </defs>
        <path d="M0,0 H397 V4 C300,12 150,45 0,120 Z" fill="url(#back-swoosh)"/>
        <rect x="0" y="240" width="397" height="198" fill="url(#back-fade)"/>
        <path d="M0,438 V424 C130,420 280,402 397,378 V438 Z" fill="url(#back-base)"/>
        <rect class="sticker-field" x="80" y="250" width="231" height="172" fill="#ffffff"/>
      </svg>
      <p class="wordmark wordmark--small">RuchKontor</p>
    </section>

    <section class="panel panel--front" aria-label="Vorderseite">
      <svg class="panel__art" viewBox="0 0 397 438" preserveAspectRatio="none" aria-hidden="true">
        <defs>
          <linearGradient id="front-fade" x1="0" y1="0" x2="0" y2="1">
            <stop offset="0" stop-color="#ffffff"/>
            <stop offset="1" stop-color="#e6e0f3"/>
          </linearGradient>
          <linearGradient id="front-wave" x1="0" y1="0" x2="1" y2="0">
            <stop offset="0" stop-color="#cdc4e6"/>
            <stop offset="1" stop-color="#7b69b3"/>
          </linearGradient>
        </defs>
        <rect x="0" y="230" width="397" height="208" fill="url(#front-fade)"/>
        <path d="M0,438 V378 C80,380 150,352 230,305 C290,270 340,262 397,262 V438 Z" fill="url(#front-wave)"/>
      </svg>
      <p class="wordmark wordmark--large">RuchKontor</p>
      <p class="sample-note">Sample<br>for you</p>
    </section>
  </main>
</body>
</html>
```